An Iconic transformation in mattress design and comfort.

“An iconic transformation in mattress design and comfort”
We are Not Kidding here!!
This is an upstart Company, BRIMO7, LLC
Our Slogan
“rest-BRIMO”

We need an outstanding web design for an outstanding product.

It took 8 years to design this bed. It was originally designed by its owner for its owner, I continue to use it every day.

With our innovative patent pending support system, with quality throughout, simplicity in design, affordable, and proudly made here in the USA, we offer a product that is superior to anything that is in the market place now. The materials that are used deviate from the industry standard, and for good reason, our product feels incredibly plush, soft, but yet provides support that can be adjusted in a simple manor, a product that will last a lifetime.
Really, why go to work if you can lay in this bed all day; you'll want to work from home! A quick nap, you'll be in heaven.

Overall Web design:
We like the web site “quietwhorl.example”, sleek, modern, a site that seems to add credibility to their product by issuing registration numbers for their tops, not a bad idea for our beds. Its important to understand that this industry is filled with smoke and mirrors, over pricing, very poor quality, and show rooms filled with sales people that are piranhas.; we seek to distance ourselves! This company will sell its product not in the traditional show room but online. Please also see these websites: www.dunelayer.example, www.tarnwick.example

Last thing I want to see is a another website filled with beds, what to do? Well perhaps a few shots of our beds is ok, after all thats what we are selling. An idea here; I was listening to a news show, this man decided to tell his story with tattoos on his own body! Interesting, different approach (not that I'm into tattoos); website design with innovation through simplicity and creative thinking and marketing.

The photos of our product have yet to be taken by a professional. We have yet to find a way to photograph this product in a different and innovative manner.

Target Market(s)

Millennials

Industry/Entity Type

It Company

Number of Pages Required

4 page

Font styles to use
Serif

Colors
ec1f27

Requirements
Must have
• Existing logo
Nice to have
• See project description
• Can further expand upon, upon request for specifics.
Should not have
• See project description

```html
<!DOCTYPE html>
<html lang="en">
<head>
<meta charset="utf-8">
<title>BRIMO7 — rest-BRIMO</title>
<link href="https://fonts.googleapis.com/css2?family=Gabriela&family=Lato:wght@400;700&display=swap" rel="stylesheet">
<style>
:root{
  --red:#c41e2e;
  --ink:#1c1c1c;
  --body:#4a4a4a;
  --muted:#777;
  --line:#dcdcdc;
  --footer:#2a2a2a;
  --white:#fff;
}
*{box-sizing:border-box;margin:0;padding:0}
html,body{width:1200px;height:2560px;overflow:hidden;background:var(--white)}
body{position:relative;font-family:'Lato',sans-serif;color:var(--body)}
.abs{position:absolute}
.serif{font-family:'Gabriela',serif}

/* header */
.contact{top:56px;display:flex;align-items:center;gap:10px;font-size:12px;color:var(--ink)}
.brand{left:0;width:1200px;top:34px;text-align:center;font-family:'Gabriela',serif;color:var(--ink)}
.brand .name{font-size:40px;line-height:44px;letter-spacing:1px}
.brand .tag{font-size:11px;line-height:14px}
.social{display:flex;gap:16px;align-items:center}
.social span{width:10px;height:10px;border-radius:50%;background:var(--ink);display:block}
.social span.on{background:var(--red)}
.nav{top:128px;left:0;width:1200px;display:flex;justify-content:center;gap:32px;font-size:15px;color:var(--ink)}
.nav .active{color:var(--red)}

/* hero */
.hero{top:163px;left:0;width:1200px;height:602px;background:linear-gradient(160deg,#8c7b62 0%,#b9a98a 35%,#d7cfc3 60%,#6b6870 100%)}
.hero-veil{inset:0;background:rgba(255,255,255,.35)}
.hero h1{top:245px;left:0;width:1200px;text-align:center;font-family:'Gabriela',serif;font-weight:400;font-size:37px;color:var(--ink)}
.hero .slogan{top:306px;left:0;width:1200px;text-align:center;font-family:'Gabriela',serif;font-size:35px;color:var(--ink);letter-spacing:1px}
.dots{top:539px;left:558px;display:flex;gap:10px}
.dots i{width:13px;height:13px;border-radius:50%;background:#111;display:block}
.dots i.on{background:var(--red)}

/* sections */
.section-title{left:0;width:1200px;text-align:center;font-family:'Gabriela',serif;font-size:27px;color:var(--red)}
.intro{top:880px;left:190px;width:820px;text-align:center;font-size:11.5px;line-height:24px;color:var(--ink)}
.band{top:999px;left:0;width:1200px;height:99px;background:var(--red)}
.band-text{left:236px;top:34px;font-size:25px;color:var(--white)}
.band-btn{left:690px;top:25px;width:273px;height:49px;border:1px solid var(--white);border-radius:4px;color:var(--white);font-size:16px;display:flex;align-items:center;justify-content:center;letter-spacing:.5px}

.promise{top:1250px;width:310px;text-align:center}
.promise svg{display:block;margin:0 auto 14px}
.promise h3{font-weight:400;font-size:18px;color:var(--red);margin-bottom:16px}
.promise p{font-size:11.5px;line-height:24px;color:var(--ink)}

/* gallery */
.gallery{top:1489px;left:0;width:1200px;height:531px;display:grid;grid-template-columns:repeat(4,300px);grid-template-rows:repeat(2,265.5px)}
.shot{position:relative}
.s1{background:linear-gradient(170deg,#7a6244 0%,#e9e6df 55%,#4b4b55 100%)}
.s2{background:linear-gradient(180deg,#8a6a3f 0%,#f2efe8 38%,#40404a 55%,#6d5a43 100%)}
.s3{background:linear-gradient(150deg,#d9cdb6 0%,#f4efe6 50%,#bba98f 100%)}
.s4{background:linear-gradient(180deg,#5a4a3a 0%,#e9e4da 45%,#4a4a54 70%,#8f7c60 100%)}
.s5{background:linear-gradient(175deg,#8f7d5c 0%,#e8e4dc 45%,#4a4a55 75%,#7a6a52 100%)}
.s6{background:linear-gradient(160deg,#6d5b43 0%,#e6dfd2 60%,#9c8a70 100%)}
.s7{background:linear-gradient(180deg,#c9a456 0%,#f3efe7 45%,#3f3f49 75%,#333 100%)}
.s8{background:linear-gradient(175deg,#8d7a5e 0%,#ebe7de 45%,#4b4b55 80%,#7a6a52 100%)}
.caption{left:0;bottom:0;width:300px;height:59px;background:var(--red);color:var(--white);font-size:16px;display:flex;align-items:center;justify-content:center}

/* testimonials & info */
.col-title{font-family:'Gabriela',serif;font-size:27px;color:var(--red)}
.testi-box{top:2135px;left:171px;width:452px;height:241px;border:1px solid var(--line)}
.testi-box p{position:absolute;left:28px;top:32px;width:396px;font-size:11px;line-height:20.5px;color:var(--ink)}
.mini-dots{left:28px;top:190px;display:flex;gap:7px}
.mini-dots i{width:8px;height:8px;border-radius:50%;background:#bbb;display:block}
.mini-dots i.on{background:var(--red)}
.btn{background:var(--red);color:var(--white);font-size:14px;font-weight:700;border-radius:4px;display:flex;align-items:center;justify-content:center}
.info{left:732px;width:267px;font-size:12.5px;line-height:21px;color:var(--body)}
.rule{left:732px;width:267px;height:1px;background:var(--line)}

/* footer */
.footer{top:2424px;left:0;width:1200px;height:136px;background:var(--footer);color:var(--white)}
.footer .social span{background:var(--white)}
.foot-links{display:flex;gap:20px;font-size:11.5px;letter-spacing:.3px}
.foot-brand{left:0;width:1200px;top:38px;text-align:center;font-family:'Gabriela',serif;font-size:44px;color:var(--white);letter-spacing:1px}
</style>
</head>
<body>

<!-- header -->
<div class="abs contact" style="left:98px">
  <svg width="14" height="14" viewBox="0 0 24 24"><path fill="#1c1c1c" d="M6.6 10.8a15.1 15.1 0 0 0 6.6 6.6l2.2-2.2a1 1 0 0 1 1-.25 11.4 11.4 0 0 0 3.6.57 1 1 0 0 1 1 1V20a1 1 0 0 1-1 1A17 17 0 0 1 3 4a1 1 0 0 1 1-1h3.5a1 1 0 0 1 1 1c0 1.25.2 2.45.57 3.6a1 1 0 0 1-.25 1z"/></svg>
  <span>555 0142 0199</span>
</div>
<div class="abs contact" style="left:232px">
  <svg width="18" height="14" viewBox="0 0 24 18"><path fill="#1c1c1c" d="M2 0h20a2 2 0 0 1 2 2v14a2 2 0 0 1-2 2H2a2 2 0 0 1-2-2V2a2 2 0 0 1 2-2zm0 3v1l10 6 10-6V3l-10 6z"/></svg>
  <span>hello@brimo7.example</span>
</div>
<div class="abs brand">
  <div class="name">BRIMO7</div>
  <div class="tag">rest-BRIMO</div>
</div>
<div class="abs social" style="left:1012px;top:60px"><span class="on"></span><span></span><span></span></div>
<nav class="abs nav">
  <span class="active">Home</span><span>About Us</span><span>Gallery</span><span>Blog</span><span>Contact Us</span>
</nav>

<!-- hero -->
<section class="abs hero" role="img" aria-label="Photo of a plush white quilted mattress on a grey quilted base in a room with a fireplace">
  <div class="abs hero-veil"></div>
  <h1 class="abs">An Iconic Transformation In Mattress Design &amp; Comfort</h1>
  <div class="abs slogan">REST - BRIMO</div>
  <div class="abs dots"><i class="on"></i><i></i><i></i><i></i></div>
</section>

<!-- intro -->
<h2 class="abs section-title" style="top:822px;font-weight:400">We're Passionate About Mattresses</h2>
<p class="abs intro">Lorem Ipsum is simply dummy text of the printing and typesetting industry. Lorem Ipsum has been the industry's standard dummy text ever since<br>the 1500s, when an unknown printer took a galley of type and scrambled it to make a type specimen book. It has survived<br>not only five centuries, but also the leap into electronic typesetting, remaining essentially unchanged.</p>

<!-- band -->
<section class="abs band">
  <div class="abs band-text">2017 New Collection Release</div>
  <div class="abs band-btn">VIEW COLLECTION</div>
</section>

<!-- promises -->
<h2 class="abs section-title" style="top:1165px;font-weight:400">Our Promises To Customers</h2>
<div class="abs promise" style="left:124px">
  <svg width="48" height="40" viewBox="0 0 48 40"><path fill="#c41e2e" d="M6 36C6 16 20 4 44 4c0 22-14 32-32 30 6-8 14-14 22-20-10 4-18 12-24 22z"/></svg>
  <h3>All Natural Materials</h3>
  <p>Lorem Ipsum is simply dummy text of the printing and typesetting industry. Lorem Ipsum has been the industry's standard dummy text ever.</p>
</div>
<div class="abs promise" style="left:448px">
  <svg width="40" height="40" viewBox="0 0 40 40"><path fill="#c41e2e" d="M2 16h7v22H2zM12 16l8-14c3 0 4 2 4 4l-2 8h12a3 3 0 0 1 3 3l-3 16a3 3 0 0 1-3 3H12z"/></svg>
  <h3>Quality Construction</h3>
  <p>Lorem Ipsum is simply dummy text of the printing and typesetting industry. Lorem Ipsum has been the industry's standard dummy text ever.</p>
</div>
<div class="abs promise" style="left:790px">
  <svg width="46" height="46" viewBox="0 0 46 46"><circle cx="23" cy="23" r="20" fill="none" stroke="#c41e2e" stroke-width="4"/><text x="23" y="33" text-anchor="middle" font-family="Lato,sans-serif" font-weight="700" font-size="28" fill="#c41e2e">$</text></svg>
  <h3>Unbeatable Prices</h3>
  <p>Lorem Ipsum is simply dummy text of the printing and typesetting industry. Lorem Ipsum has been the industry's standard dummy text ever.</p>
</div>

<!-- gallery -->
<section class="abs gallery">
  <div class="shot s1" role="img" aria-label="Mattress corner beside a fireplace"></div>
  <div class="shot s2" role="img" aria-label="Close view of the quilted mattress side panel"></div>
  <div class="shot s3" role="img" aria-label="Close view of the soft plush mattress top"></div>
  <div class="shot s4" role="img" aria-label="Mattress side panel in a warm room"></div>
  <div class="shot s5" role="img" aria-label="Mattress in front of a window and plant"></div>
  <div class="shot s6" role="img" aria-label="Soft focus detail of the plush top layer"></div>
  <div class="shot s7" role="img" aria-label="Mattress edge with fireplace behind">
    <div class="abs caption">Simply Dummy Text</div>
  </div>
  <div class="shot s8" role="img" aria-label="Full mattress on the floor near a fireplace"></div>
</section>

<!-- testimonials -->
<h2 class="abs col-title" style="left:171px;top:2081px;font-weight:400">Testimonals</h2>
<div class="abs testi-box">
  <p>Lorem Ipsum is simply dummy text of the printing and typesetting industry. Lorem Ipsum has been the industry's standard dummy text ever since the 1500s, when an unknown printer took a galley of type and scrambled it to make a type specimen book. It has survived not only five centuries, but also the leap into electronic typesetting, remaining essentially unchanged. It was popularised in the 1960s with the release of Letraset sheets containing Lorem Ipsum passages</p>
  <div class="abs mini-dots"><i class="on"></i><i></i><i></i></div>
  <div class="abs btn" style="left:351px;top:180px;width:66px;height:33px">more</div>
</div>

<!-- popular info -->
<h2 class="abs col-title" style="left:732px;top:2081px;font-weight:400">Popular Info</h2>
<p class="abs info" style="top:2137px">Lorem Ipsum is simply dummy text of the infor printing and typesetting industry.</p>
<div class="abs rule" style="top:2190px"></div>
<p class="abs info" style="top:2204px">Lorem Ipsum is simply dummy text of the infor printing and typesetting industry.</p>
<div class="abs rule" style="top:2262px"></div>
<p class="abs info" style="top:2276px">Lorem Ipsum is simply dummy text of the infor printing and typesetting industry.</p>
<div class="abs btn" style="left:734px;top:2338px;width:65px;height:33px">more</div>

<!-- footer -->
<footer class="abs footer">
  <div class="abs social" style="left:138px;top:63px"><span></span><span></span><span></span></div>
  <div class="abs foot-links" style="left:302px;top:62px"><span>ABOUT</span><span>BLOG</span><span>CONTACT</span></div>
  <div class="abs foot-brand">BRIMO7</div>
  <div class="abs foot-links" style="left:798px;top:62px"><span>PRIVACY</span><span>TERMS &amp; CONDITION</span></div>
</footer>

</body>
</html>
```